New Design for Willow Glow & Laser

The name of our company is Willow Glow & Laser, and this is our current website: www.WillowGlowLaser.example. We are looking for a fresh design mock-up of our website.
What is important to us?
> We want to maintain the same navigation.
> We want to use the same content (e.g., text, pictures, etc.)
> We want to maintain the color scheme.
> The website aims to get visitors to BOOK ONLINE or BUY ONLINE.
Essential instructions for designers:
> Please visit our current website and our social media accounts to get a better idea of our brand design.
> We want a mockup design for our home page, service page, pricing page, before & after page, shop deals page, careers page, contact pages, and blog pages.
> Color codes: #faa641, #222222, #fffffe, #ea8103
Target Market(s)
women 25 - 45
Number of Pages Required
5+ page
Look and feel

```html
<!DOCTYPE html>
<html lang="en">
<head>
<meta charset="utf-8">
<title>Willow Glow &amp; Laser — Home</title>
<link href="https://fonts.googleapis.com/css2?family=Poppins:wght@400;500;600;700&display=swap" rel="stylesheet">
<style>
:root{
  --orange:#faa641;
  --orange-deep:#ea8103;
  --ink:#222222;
  --white:#fffffe;
  --soft:#f3f3f3;
  --muted:#555555;
  --dark:#161616;
}
*{box-sizing:border-box;margin:0;padding:0}
html,body{width:1200px;height:4373px;overflow:hidden}
body{position:relative;background:var(--white);font-family:'Poppins',sans-serif;color:var(--ink)}
.abs{position:absolute}
.btn{position:absolute;display:flex;align-items:center;justify-content:center;background:var(--orange);color:var(--white);font-weight:500;border-radius:6px;text-transform:uppercase}
.arrow{position:absolute;width:38px;height:38px;border-radius:50%;display:flex;align-items:center;justify-content:center}
.arrow.dark{background:var(--ink)}
.arrow.lite{background:var(--orange)}
.photo{position:absolute;border-radius:14px}
.section-title{position:absolute;left:0;width:1200px;text-align:center;font-weight:600;font-size:42px}

/* top bar */
.topbar{left:0;top:0;width:1200px;height:38px;background:var(--ink)}
.topbar .dot{position:absolute;top:9px;width:16px;height:16px;border:1.5px solid var(--white);border-radius:50%}
.topbar .info{position:absolute;top:9px;color:var(--white);font-size:15px;display:flex;align-items:center;gap:8px}

/* nav */
.nav{left:0;top:38px;width:1200px;height:100px;background:var(--white);border-bottom:1px solid #eee}
.brand{position:absolute;display:flex;align-items:center;gap:10px;font-weight:700;color:var(--ink)}
.brand .mark{border-radius:50%;background:var(--orange)}
.menu{position:absolute;left:460px;top:40px;display:flex;gap:32px;font-size:13px;text-transform:uppercase}
.menu .active{color:var(--orange)}

/* hero */
.hero{left:0;top:138px;width:1200px;height:682px;background:#f2f2f2}
.hero-title-a{left:628px;top:268px;font-size:66px;font-weight:600;color:var(--orange);line-height:1}
.hero-title-b{left:628px;top:340px;font-size:86px;font-weight:700;line-height:1}
.hero-sub{left:633px;top:445px;width:480px;font-size:17px;line-height:29px}

/* offers */
.card-title{position:absolute;width:245px;text-align:center;font-weight:600;font-size:18px}
.card-text{position:absolute;width:220px;text-align:center;font-size:11.5px;line-height:19px;color:var(--muted)}
.card-link{position:absolute;width:245px;text-align:center;font-size:12.5px;color:var(--orange);text-decoration:underline;font-weight:500}

/* about */
.about{left:0;top:1405px;width:1200px;height:703px;background:var(--soft)}
.about h2{position:absolute;left:634px;top:125px;font-size:36px;font-weight:600}
.about p{position:absolute;left:634px;width:485px;font-size:14.5px;line-height:31px;color:#444}

/* cta */
.cta{left:0;top:2108px;width:1200px;height:492px;background:linear-gradient(120deg,#2a2a2a,#121212 55%,#262626)}
.cta h2{position:absolute;left:0;width:1200px;top:112px;text-align:center;color:var(--white);font-size:46px;font-weight:600}
.cta p{position:absolute;left:240px;width:720px;top:190px;text-align:center;color:var(--white);font-size:15.5px;line-height:31px}

/* testimonials */
.avatar{position:absolute;width:90px;height:90px;border-radius:50%;background:linear-gradient(135deg,#d9d2cc,#9a8f86)}
.quote{position:absolute;width:215px;font-size:12px;line-height:19.5px;color:var(--muted);text-align:justify}
.quote b{color:var(--orange);font-size:24px;font-weight:700;line-height:0;margin-right:8px;vertical-align:-6px}
.client{position:absolute;font-weight:600;font-size:14px}
.stars{position:absolute;color:var(--orange);font-size:12px;letter-spacing:1px}

/* contact band */
.band{left:0;top:3057px;width:1200px;height:128px;background:var(--dark)}
.band h3{position:absolute;left:154px;top:40px;color:var(--white);font-size:32px;font-weight:600}

/* newsletter + footer */
.footer{left:0;top:3808px;width:1200px;height:565px;background:var(--dark)}
.newsletter{left:647px;top:3749px;width:553px;height:129px;background:var(--orange)}
.newsletter h4{position:absolute;left:79px;top:18px;font-size:26px;font-weight:600;color:var(--white)}
.newsletter .field{position:absolute;left:72px;top:60px;width:400px;height:44px;border-radius:22px;background:var(--white);font-size:11px;color:#777;padding:14px 26px}
.newsletter .go{position:absolute;left:350px;top:60px;width:122px;height:44px;border-radius:22px;background:var(--dark);color:var(--white);font-size:15px;font-weight:500;display:flex;align-items:center;justify-content:center}
.f-head{position:absolute;color:var(--white);font-size:25px;font-weight:500}
.f-ic{position:absolute;width:40px;height:40px;border-radius:50%;background:var(--orange);display:flex;align-items:center;justify-content:center}
.f-label{position:absolute;color:var(--white);font-size:16px;font-weight:500}
.f-val{position:absolute;color:var(--white);font-size:15px;line-height:21px}
.f-link{position:absolute;color:var(--white);font-size:16px;display:flex;align-items:center;gap:12px}
.f-link i{display:block;width:13px;height:13px;border-radius:50%;background:var(--orange)}
.social{position:absolute;width:34px;height:34px;border-radius:50%;border:2px solid var(--orange)}
.legal{position:absolute;top:4320px;color:var(--white);font-size:13px}
</style>
</head>
<body>

<!-- top bar -->
<div class="abs topbar">
  <span class="dot" style="left:88px"></span><span class="dot" style="left:108px"></span>
  <span class="dot" style="left:128px"></span><span class="dot" style="left:148px"></span>
  <div class="info" style="left:715px">
    <svg width="16" height="16" viewBox="0 0 24 24"><path d="M6.6 10.8a15 15 0 0 0 6.6 6.6l2.2-2.2c.3-.3.7-.4 1-.2 1.1.4 2.3.6 3.6.6.6 0 1 .4 1 1V20c0 .6-.4 1-1 1A17 17 0 0 1 3 4c0-.6.4-1 1-1h3.5c.6 0 1 .4 1 1 0 1.3.2 2.5.6 3.6.1.3 0 .7-.2 1z" fill="#faa641"/></svg>
    (555) 014-2290
  </div>
  <div class="info" style="left:880px">
    <svg width="16" height="12" viewBox="0 0 16 12"><rect width="16" height="12" rx="1.5" fill="#faa641"/><path d="M1 1l7 5 7-5" stroke="#222" stroke-width="1.4" fill="none"/></svg>
    hello@willowglowlaser.example
  </div>
</div>

<!-- navigation -->
<div class="abs nav">
  <div class="brand" style="left:88px;top:26px;font-size:24px;letter-spacing:1px">
    <span class="mark" style="width:30px;height:30px"></span>WILLOW GLOW &amp; LASER
  </div>
  <nav class="menu">
    <span class="active">Home</span><span>Services ▾</span><span>Pricing ▾</span><span>About ▾</span><span>Blog</span><span>Contact</span>
  </nav>
  <div class="abs" style="left:453px;top:64px;width:56px;height:2px;background:var(--orange)"></div>
  <div class="btn" style="left:955px;top:27px;width:160px;height:44px;font-size:14px">Book Online</div>
</div>

<!-- hero -->
<section class="abs hero">
  <div class="abs" role="img" aria-label="Smiling client holding a hand mirror with a beaming skin technician behind her" style="left:0;top:0;width:610px;height:682px;background:linear-gradient(135deg,#d8d4cf,#b9a596 55%,#8a6e5e)"></div>
</section>
<div class="abs hero-title-a">Your skin</div>
<div class="abs hero-title-b">Deserves It</div>
<div class="abs hero-sub">LASER CENTER &amp; MEDISPA located in Downtown Phoenix, Tempe, Tucson, &amp; Yuma.</div>
<div class="btn" style="left:633px;top:539px;width:201px;height:70px;font-size:19px;text-transform:uppercase">Book Online</div>

<!-- what we offer -->
<h2 class="section-title" style="top:918px">What We Offer</h2>
<div class="arrow dark" style="left:23px;top:1163px"><svg width="12" height="12" viewBox="0 0 12 12"><path d="M8 1L3 6l5 5" stroke="#fff" stroke-width="2" fill="none"/></svg></div>
<div class="arrow lite" style="left:1138px;top:1163px"><svg width="12" height="12" viewBox="0 0 12 12"><path d="M4 1l5 5-5 5" stroke="#fff" stroke-width="2" fill="none"/></svg></div>

<div class="photo" role="img" aria-label="Client wearing protective goggles receiving a light facial treatment" style="left:85px;top:1018px;width:245px;height:158px;background:linear-gradient(135deg,#c9c2bb,#8f7f74)"></div>
<div class="card-title" style="left:85px;top:1193px">Photofacials</div>
<div class="card-text" style="left:97px;top:1227px">An photofacial is a light treatment that uses an FDA-approved device to deliver an arc of light energy that penetrates all levels of the skin.</div>
<div class="card-link" style="left:85px;top:1314px">READ MORE</div>

<div class="photo" role="img" aria-label="Client receiving an injection in the brow area" style="left:347px;top:1018px;width:245px;height:158px;background:linear-gradient(135deg,#d7cdc6,#6e5b52)"></div>
<div class="card-title" style="left:347px;top:1193px">Smoothtox Injections</div>
<div class="card-text" style="left:359px;top:1227px">Today Lumexa and Smoothtox are the most trusted and widely used injectable neuromodulators. Smoothtox is made by Marlow Labs and Lumexa</div>
<div class="card-link" style="left:347px;top:1314px">READ MORE</div>

<div class="photo" role="img" aria-label="Laser hair removal device applied to an underarm" style="left:610px;top:1018px;width:245px;height:158px;background:linear-gradient(135deg,#c8c5c2,#7d746e)"></div>
<div class="card-title" style="left:610px;top:1193px">Laser Hair Removal</div>
<div class="card-text" style="left:622px;top:1227px">You go to shave your legs (or chest or, wink, wink, other body parts) right before that big date and end up bleeding like crazy</div>
<div class="card-link" style="left:610px;top:1314px">READ MORE</div>

<div class="photo" role="img" aria-label="Gloved hands performing microneedling on a client's forehead" style="left:870px;top:1018px;width:245px;height:158px;background:linear-gradient(135deg,#d3cfcb,#5d5652)"></div>
<div class="card-title" style="left:870px;top:1193px">Microneedling</div>
<div class="card-text" style="left:882px;top:1227px">Our skin is the most valuable real estate that the human body has. It is essential that we feel comfortable and confident in our skin.</div>
<div class="card-link" style="left:870px;top:1314px">READ MORE</div>

<!-- about -->
<section class="abs about">
  <div class="photo" role="img" aria-label="Client admiring her skin in a hand mirror" style="left:63px;top:88px;width:490px;height:510px;background:linear-gradient(135deg,#e5e2df,#b59a86 60%,#6b5247)"></div>
  <h2>About Willow Glow &amp; Laser</h2>
  <p style="top:212px">At Willow Glow &amp; Laser, we’ve always believed that caring about your skin and your appearance is not selfish, it is self-care. It’s time to be proud of the steps you take to look your best and it’s time you ask for the best. Your skin deserves it.</p>
  <p style="top:367px">Willow Glow brings to you the latest technology, techniques, and the best professionals to deliver the results you want guaranteed.</p>
  <div class="btn" style="left:634px;top:490px;width:187px;height:58px;font-size:14px">Read More</div>
</section>

<!-- call to action -->
<section class="abs cta" role="img" aria-label="Dimmed photo of a client receiving a laser treatment">
  <h2>Get Your Treatment Right Away!</h2>
  <p>Lorem ipsum dolor sit amet, consectetur adipiscing elit. Nulla convallis lectus nunc. Sed tris tique quam in ligula posu ere dapibus. Cras sodales, magna nec imperdiet porta</p>
  <div class="btn" style="left:476px;top:305px;width:248px;height:73px;font-size:19px;border-radius:14px">Book Online</div>
</section>

<!-- testimonials -->
<h2 class="section-title" style="top:2697px">What Our Happy Clients Say</h2>
<div class="arrow dark" style="left:23px;top:2860px"><svg width="12" height="12" viewBox="0 0 12 12"><path d="M8 1L3 6l5 5" stroke="#fff" stroke-width="2" fill="none"/></svg></div>
<div class="arrow lite" style="left:1141px;top:2860px"><svg width="12" height="12" viewBox="0 0 12 12"><path d="M4 1l5 5-5 5" stroke="#fff" stroke-width="2" fill="none"/></svg></div>

<div class="avatar" role="img" aria-label="Client portrait" style="left:85px;top:2818px"></div>
<div class="quote" style="left:195px;top:2820px"><b>“</b>She explained the procedure to me, answered all questions and did a great job at making me feel at ease. I would absolutely recommend Willow Glow &amp; Laser.</div>
<div class="client" style="left:196px;top:2938px">Rosa L.</div><div class="stars" style="left:196px;top:2960px">★★★★★</div>

<div class="avatar" role="img" aria-label="Client portrait" style="left:438px;top:2818px"></div>
<div class="quote" style="left:548px;top:2820px"><b>“</b>I have been going to Willow Glow &amp; Laser for 2 years now. I am very pleased with my laser hair reduction results.</div>
<div class="client" style="left:549px;top:2938px">Mia K.</div><div class="stars" style="left:549px;top:2960px">★★★★★</div>

<div class="avatar" role="img" aria-label="Client portrait" style="left:790px;top:2818px"></div>
<div class="quote" style="left:900px;top:2820px"><b>“</b>Tess is my technician and I love her! Always goes the extra mile to make sure areas are covered, and that I’m getting the best result. I couldn’t be happier.</div>
<div class="client" style="left:901px;top:2938px">Tess B.</div><div class="stars" style="left:901px;top:2960px">★★★★★</div>

<!-- contact band -->
<section class="abs band">
  <svg class="abs" style="left:88px;top:45px" width="52" height="40" viewBox="0 0 52 40"><path d="M2 2l18 18L2 38h12l18-18L14 2z" fill="#faa641"/><path d="M20 2l18 18-18 18h12l18-18L32 2z" fill="#ea8103"/></svg>
  <h3>If you have any questions, please contact us.</h3>
  <div class="btn" style="left:913px;top:28px;width:200px;height:70px;font-size:19px">Get In Touch</div>
</section>

<!-- gallery -->
<h2 class="section-title" style="top:3270px;font-size:50px">Gallery</h2>
<div class="arrow dark" style="left:23px;top:3487px"><svg width="12" height="12" viewBox="0 0 12 12"><path d="M8 1L3 6l5 5" stroke="#fff" stroke-width="2" fill="none"/></svg></div>
<div class="arrow lite" style="left:1141px;top:3487px"><svg width="12" height="12" viewBox="0 0 12 12"><path d="M4 1l5 5-5 5" stroke="#fff" stroke-width="2" fill="none"/></svg></div>
<div class="photo" role="img" aria-label="Client in a treatment room holding a mirror" style="left:87px;top:3357px;width:331px;height:293px;background:linear-gradient(135deg,#e9e7e4,#a08c7e 60%,#3b3330)"></div>
<div class="photo" role="img" aria-label="Specialist consulting with a client using a tablet" style="left:434px;top:3357px;width:331px;height:293px;background:linear-gradient(135deg,#eae6e2,#b8aba0 55%,#5a4f49)"></div>
<div class="photo" role="img" aria-label="Technician treating a smiling client" style="left:781px;top:3357px;width:331px;height:293px;background:linear-gradient(135deg,#efece9,#c4b0a0 50%,#2e2a28)"></div>

<!-- footer -->
<footer class="abs footer">
  <div class="abs" style="left:88px;top:117px;width:1030px;height:1px;background:var(--orange-deep)"></div>
  <div class="brand" style="left:175px;top:230px;font-size:27px;color:var(--white);letter-spacing:1px">
    <span class="mark" style="width:44px;height:44px"></span>WILLOW GLOW<br>&amp; LASER
  </div>
  <span class="social" style="left:235px;top:358px"></span><span class="social" style="left:278px;top:358px"></span>
  <span class="social" style="left:321px;top:358px"></span><span class="social" style="left:364px;top:358px"></span>

  <div class="f-head" style="left:537px;top:160px">Address</div>
  <div class="f-ic" style="left:537px;top:233px"><svg width="16" height="20" viewBox="0 0 16 20"><path d="M8 0a7 7 0 0 0-7 7c0 5 7 13 7 13s7-8 7-13a7 7 0 0 0-7-7zm0 10a3 3 0 1 1 0-6 3 3 0 0 1 0 6z" fill="#fff"/></svg></div>
  <div class="f-label" style="left:605px;top:228px">ADDRESS</div>
  <div class="f-val" style="left:605px;top:250px">2200 Larkspur Lane Suite 40<br>Phoenix, AZ 85000</div>
  <div class="f-ic" style="left:537px;top:322px"><svg width="18" height="18" viewBox="0 0 24 24"><path d="M6.6 10.8a15 15 0 0 0 6.6 6.6l2.2-2.2c.3-.3.7-.4 1-.2 1.1.4 2.3.6 3.6.6.6 0 1 .4 1 1V20c0 .6-.4 1-1 1A17 17 0 0 1 3 4c0-.6.4-1 1-1h3.5c.6 0 1 .4 1 1 0 1.3.2 2.5.6 3.6.1.3 0 .7-.2 1z" fill="#fff"/></svg></div>
  <div class="f-label" style="left:605px;top:318px">PHONE NUMBER</div>
  <div class="f-val" style="left:605px;top:342px">(555) 014-2290</div>
  <div class="f-ic" style="left:537px;top:400px"><svg width="18" height="13" viewBox="0 0 16 12"><rect width="16" height="12" rx="1.5" fill="#fff"/><path d="M1 1l7 5 7-5" stroke="#faa641" stroke-width="1.4" fill="none"/></svg></div>
  <div class="f-label" style="left:605px;top:396px">EMAIL US</div>
  <div class="f-val" style="left:605px;top:420px">hello@willowglowlaser.example</div>

  <div class="f-head" style="left:884px;top:162px">Quick Links</div>
  <div class="f-link" style="left:884px;top:223px"><i></i>Services</div>
  <div class="f-link" style="left:884px;top:264px"><i></i>Pricing</div>
  <div class="f-link" style="left:884px;top:305px"><i></i>About</div>
  <div class="f-link" style="left:884px;top:346px"><i></i>Blog</div>
  <div class="f-link" style="left:884px;top:387px"><i></i>Contact</div>

  <div class="abs" style="left:88px;top:487px;width:1030px;height:1px;background:var(--orange-deep)"></div>
</footer>
<div class="legal" style="left:90px">© 2024 Willow Glow &amp; Laser. All Rights Reserved. – Privacy Policy • Terms &amp; Conditions</div>
<div class="legal" style="left:713px">Medical Director: Dr. Alan Merrow, NMD License #00-0000</div>

<section class="abs newsletter">
  <h4>Our Newsletter Sign Up</h4>
  <div class="field">Enter Email Address</div>
  <div class="go">SIGNUP</div>
</section>

</body>
</html>
```